Small B&W Ear Panel Spa Newspaper Ad

We need a redesign for our Daily Ear Panel Newspaper Advertisement which appears in Harbor Ledger daily newspaper in Dubai.
The advert is small, size 40mm x 25mm, and it is in B&W, or black, grey and white.
The advert is for Willowstone Spa and Massage Centres.
We attach the current pdf file which we use - the information included in the current ad is :
willowstone
Balinese Massage Centres
Spa
800 KNEADER
British Owned & Managed
www.willowstone-example.ae
The advert is very small, and the MINIMUM information we would like to include is :
willowstone
Spa
800 KNEADER
ww.willowstone-example.ae
It is optional to include the extra information :
Balinese Massage Centres
British Owned & Managed
The main brief is that the Advert must be BOLD & EYE-CATCHING.
iT MAY BE BEST TO KEEP THE ADVERT SIMPLE IN ORDER TO ACHIEVE THIS.
We like the current "rounded" edges to the box.
It may be best to use shades of black, grey and white.
We attach also 2 pictures of the front page of the Newspaper so that you can see how the Ad sits on the page, and how small it is.
The advert appears every day, so it must also be memorable, so that readers become used to it, whilst it still attracts their attention.
ONE POSSIBLE IDEA - PERHAPS THE ADVERT CAN BE A CIRCULAR, ROUND OR OVAL DESIGN, WHICH WOULD GIVE MORE BLANK WHITE SPACE AROUND IT, SO THAT IT WOULD STAND OUT MORE.

```html
<!DOCTYPE html>
<html lang="en">
<head>
<meta charset="utf-8">
<title>Willowstone Spa – Ear Panel Ad</title>
<link rel="stylesheet" href="https://fonts.googleapis.com/css2?family=Montserrat:wght@600;700&family=Poppins:wght@300;600&display=swap">
<style>
  :root {
    --ink: #000000;
    --paper: #ffffff;
    --edge: #d6d6d6;
    --canvas: #ffffff;
  }
  html, body {
    margin: 0;
    padding: 0;
    width: 1200px;
    height: 1200px;
    overflow: hidden;
    background: var(--canvas);
  }
  .ad {
    position: absolute;
    left: 102px;
    top: 280px;
    width: 993px;
    height: 629px;
    background: var(--ink);
    box-shadow: 0 0 0 1px var(--edge), 1px 2px 4px rgba(0,0,0,0.25);
    overflow: hidden;
  }
  .ad__waves {
    position: absolute;
    inset: 0;
    width: 100%;
    height: 100%;
  }
  .ad__line {
    position: absolute;
    left: 0;
    width: 100%;
    text-align: center;
    color: var(--paper);
    line-height: 1;
    transform: translateY(-50%);
    white-space: nowrap;
  }
  .brand-name {
    top: 160px;
    font-family: "Poppins", sans-serif;
    font-weight: 600;
    font-size: 136px;
    letter-spacing: -1px;
  }
  .tagline {
    top: 244px;
    font-family: "Poppins", sans-serif;
    font-weight: 600;
    font-size: 36px;
    letter-spacing: 0.2em;
    padding-left: 0.2em;
    box-sizing: border-box;
  }
  .service {
    top: 336px;
    font-family: "Poppins", sans-serif;
    font-weight: 300;
    font-size: 118px;
    color: transparent;
    -webkit-text-stroke: 2px var(--paper);
  }
  .phone {
    top: 460px;
    display: flex;
    justify-content: center;
    align-items: center;
    gap: 22px;
    font-family: "Montserrat", sans-serif;
    font-weight: 700;
    font-size: 84px;
  }
  .phone__icon {
    width: 86px;
    height: 74px;
    fill: var(--paper);
  }
  .web {
    position: absolute;
    right: 14px;
    bottom: 14px;
    color: var(--paper);
    font-family: "Montserrat", sans-serif;
    font-weight: 700;
    font-size: 34px;
    line-height: 1;
  }
</style>
</head>
<body>
  <div class="ad">
    <svg class="ad__waves" viewBox="0 0 518 328" preserveAspectRatio="none" aria-hidden="true">
      <path fill="var(--paper)" d="M0,0 H518 V52 C470,44 430,32 380,26 C300,18 150,16 0,28 Z"/>
      <path fill="var(--paper)" d="M0,270 C140,258 300,268 518,284 V294 C330,284 150,282 0,293 Z"/>
    </svg>

    <div class="ad__line brand-name">willowstone</div>
    <div class="ad__line tagline">Balinese Massage Centre</div>
    <div class="ad__line service">SPA</div>
    <div class="ad__line phone">
      <svg class="phone__icon" viewBox="0 0 86 74" aria-hidden="true">
        <path d="M6,14 C6,6 18,2 43,2 C68,2 80,6 80,14 L80,22 L62,24 L60,16 C52,13 34,13 26,16 L24,24 L6,22 Z"/>
        <path d="M28,26 L58,26 L76,50 L76,70 L10,70 L10,50 Z"/>
        <g fill="var(--ink)">
          <rect x="29" y="38" width="7" height="6"/><rect x="40" y="38" width="7" height="6"/><rect x="51" y="38" width="7" height="6"/>
          <rect x="27" y="48" width="7" height="6"/><rect x="40" y="48" width="7" height="6"/><rect x="53" y="48" width="7" height="6"/>
          <rect x="25" y="58" width="7" height="6"/><rect x="40" y="58" width="7" height="6"/><rect x="55" y="58" width="7" height="6"/>
        </g>
      </svg>
      <span class="phone__number">800 KNEADER</span>
    </div>
    <div class="web">www.willowstone-example.ae</div>
  </div>
</body>
</html>
```